Pelvane Global Media
Business Card. Letterhead and Envelope.
Pelvane Global Media  - Communications and Media
Creative Brief
Professional
Tomas Wyck-Field
Managing Director - Europe
Fenmoor House Ashbury Row Tillington Kent ME9 4QZ UK
tomas.wyckfield@pelvanemedia.example
www.pelvanemedia.example
I would like to see our logo plus a listing of our office locations included please. The office locations listed in upper case please but not in bold and not too big. They are: Amsterdam, London, Munich, New York, San Francisco.

```html
<!DOCTYPE html>
<html lang="en">
<head>
<meta charset="utf-8">
<title>Pelvane Global Media – Stationery</title>
<link rel="stylesheet" href="https://fonts.googleapis.com/css2?family=Montserrat:wght@600&family=Open+Sans:wght@400;600&display=swap">
<style>
:root{
  --bg-top:#3a3a3c;
  --bg-bottom:#1c1c1d;
  --blue:#2f6fb6;
  --blue-dark:#1f4f8a;
  --paper:#ffffff;
  --ink:#3a3a3a;
  --grey:#8a8a8a;
  --black:#111112;
  --caption:#9a9a9a;
}
*{box-sizing:border-box;margin:0;padding:0}
html,body{width:1200px;height:463px;overflow:hidden}
body{background:linear-gradient(180deg,var(--bg-top),var(--bg-bottom));font-family:"Open Sans",sans-serif;color:var(--ink);position:relative}
.brand{display:flex;align-items:center;gap:8px}
.brand-mark{width:14px;height:14px;background:var(--blue);flex:none}
.brand-name{font-family:"Montserrat",sans-serif;font-weight:600;color:var(--blue);letter-spacing:1px;line-height:1}
.brand-name.light{color:#fff}
.hero{position:absolute;left:180px;top:98px}
.hero .brand-mark{width:30px;height:30px}
.hero .brand-name{font-size:21px;color:#fff}
.hero .sub{font-size:9px;color:#cfcfcf;margin:6px 0 0 38px}
.hero .concept{font-size:8px;color:#8fb6e0;margin:4px 0 0 38px}
.card{position:absolute;width:180px;height:100px;background:var(--paper);padding:10px 12px;border-left:4px solid var(--blue);overflow:hidden}
.card.dark{background:var(--black);border-left:none;display:flex;align-items:center;justify-content:center}
.card .brand-name{font-size:12px}
.card .brand-mark{width:10px;height:10px}
.card small{display:block;font-size:5px;line-height:1.55;color:var(--grey)}
.card .name{font-size:6px;font-weight:600;color:var(--ink)}
.card .role{font-size:5px;color:var(--blue)}
.card-details{margin:8px 0 0 46px}
.offices{font-size:5px;color:var(--blue);letter-spacing:.6px;line-height:1.7;margin-top:36px}
.caption{position:absolute;font-size:6px;color:var(--caption);width:180px;text-align:center}
.letterhead{position:absolute;left:456px;top:24px;width:252px;height:410px;background:var(--paper);border-left:6px solid var(--blue);padding:18px 16px}
.letterhead .brand-name{font-size:13px}
.letterhead .tag{font-size:5px;color:var(--grey);margin:3px 0 0 22px}
.watermark{position:absolute;left:76px;top:150px;width:90px;height:90px;background:#f0f0f0;border-radius:6px}
.letterhead .footer{position:absolute;left:16px;right:16px;bottom:10px;font-size:4.5px;color:var(--grey);text-align:center;line-height:1.6;border-top:1px solid #e4e4e4;padding-top:4px}
.envelopes{position:absolute;left:720px;top:40px}
.env-front{position:absolute;left:775px;top:300px;width:350px;height:132px;padding:10px 14px}
.env-front .brand-name{font-size:11px}
.env-front .brand-mark{width:9px;height:9px}
.env-front .addr{font-size:4.5px;color:var(--grey);margin:3px 0 0 17px}
</style>
</head>
<body>

<header class="hero">
  <div class="brand"><span class="brand-mark"></span><span class="brand-name">PELVANE</span></div>
  <p class="sub">Pelvane Global Media</p>
  <p class="concept">Stationery Concepts</p>
</header>

<section class="card" style="left:79px;top:235px">
  <div class="brand"><span class="brand-mark"></span><span class="brand-name">PELVANE</span></div>
  <div style="display:flex;justify-content:space-between;margin-top:30px">
    <div><p class="name">Tomas Wyck-Field</p><p class="role">Managing Director - Europe</p></div>
    <small>T +44 1795 555014<br>M +44 7700 900123<br>F +44 1795 555015</small>
  </div>
</section>
<p class="caption" style="left:79px;top:340px">Business Card Front</p>

<section class="card" style="left:266px;top:235px">
  <div class="brand"><span class="brand-mark"></span><span class="brand-name">PELVANE</span></div>
  <div class="card-details">
    <p class="name">Tomas Wyck-Field</p><p class="role">Managing Director - Europe</p>
    <small style="margin-top:4px">Fenmoor House<br>Ashbury Row, Tillington<br>Kent ME9 4QZ UK<br>tomas.wyckfield@pelvanemedia.example<br>www.pelvanemedia.example</small>
  </div>
</section>
<p class="caption" style="left:266px;top:340px">Business Card Back</p>

<section class="card" style="left:79px;top:352px;height:84px">
  <p class="offices">AMSTERDAM · LONDON · MUNICH<br>NEW YORK · SAN FRANCISCO</p>
</section>
<p class="caption" style="left:79px;top:440px">Alt Card Front</p>

<section class="card dark" style="left:266px;top:352px;height:84px">
  <div class="brand"><span class="brand-mark"></span><span class="brand-name light">PELVANE</span></div>
</section>
<p class="caption" style="left:266px;top:440px">Alt Card Back</p>

<section class="letterhead">
  <div class="brand"><span class="brand-mark"></span><span class="brand-name">PELVANE</span></div>
  <p class="tag">Pelvane Global Media</p>
  <div class="watermark" role="img" aria-label="Faint brand square"></div>
  <p class="footer">Fenmoor House Ashbury Row Tillington Kent ME9 4QZ UK · www.pelvanemedia.example<br>AMSTERDAM · LONDON · MUNICH · NEW YORK · SAN FRANCISCO</p>
</section>
<p class="caption" style="left:492px;top:440px">Letterhead</p>

<svg class="envelopes" width="420" height="400" viewBox="0 0 420 400" aria-hidden="true">
  <rect x="40" y="20" width="360" height="150" fill="#141415"/>
  <polygon points="40,20 220,110 400,20" fill="#2a2a2c"/>
  <rect x="60" y="90" width="350" height="140" fill="#f4f4f4"/>
  <polygon points="60,90 235,160 410,90" fill="var(--blue)"/>
  <polygon points="60,90 235,140 410,90" fill="var(--blue-dark)"/>
  <rect x="140" y="112" width="18" height="18" fill="#fff"/>
  <rect x="55" y="150" width="350" height="150" fill="#e9e9e9"/>
  <polygon points="55,150 230,230 405,150" fill="#dcdcdc"/>
  <rect x="150" y="165" width="16" height="16" fill="var(--blue)"/>
  <rect x="55" y="260" width="353" height="132" fill="#fff"/>
  <rect x="55" y="386" width="353" height="6" fill="var(--blue)"/>
</svg>
<section class="env-front">
  <div class="brand"><span class="brand-mark"></span><span class="brand-name">PELVANE</span></div>
  <p class="addr">Fenmoor House Ashbury Row Tillington Kent ME9 4QZ UK</p>
</section>
<p class="caption" style="left:860px;top:440px">Envelopes</p>

</body>
</html>
```